Fun & Healthy Dog Treat Business Needs a Business & Loyalty Card

We need a business card design for a business that provides healthy dog products.

The design should communicate a healthy aspect and should communicate that the business focuses on healthy produce.

We would like some aspects if not all of our current logo to appear on the card.

We would also like a two sided card with the back of the card being able to be used as a loyalty program where after purchasing 7 items the buyer receives a free gift. There should be a way of identifying how many purchases a customer has made and if possible enable at least 4 - 5 gives be able to be given on one card. ie make 7 purchases and receive a give, to be able to be done 4 - 5 times before they need to be given a new card.

Rather than the focus be solely on dog treats we would like the card's focus to be a bit wider should we decide to enter other markets in the future and therefore not mention dog treats.

We want the card to be colourful while still retaining a very healthy aspect.

We also need the card to have pictures such as a dog or dogs head that enable us to determine how many items a customer has purchase before we give them a free gift.

Please see our website for further details regarding our business including contact details. www.wrenfieldpantry.com.au

Target Market(s)

Dog lovers who are health concious

Industry/Entity Type

Pet

Contact Information for Business Card

Products for Healthy Dogs
Web Address - www.wrenfieldpantry.com.au
Email address - info@wrenfieldpantry.com.au

Font styles to use
Serif

Colors
acd037
f04a50

Requirements
Must have
• Wrenfield Pantry
• Products for Healthy Dogs
• Web Address - www.wrenfieldpantry.com.au
• Email address - info@wrenfieldpantry.com.au
• Mobile Number - 0417 358 619
Nice to have
• Part of our current logo
• Blend in with current logo but not include the words healthy dog treats
• The flip side of the card should have a Loyalty Program where when you purchase 7 products you receive a free gift.
Should not have
• Should not include the words healthy dog treats
• Should not have the fixed line phone number

```html
<!DOCTYPE html>
<html lang="en">
<head>
<meta charset="utf-8">
<title>Wrenfield Pantry – Business &amp; Loyalty Card</title>
<link rel="stylesheet" href="https://fonts.googleapis.com/css2?family=PT+Serif:wght@400;700&display=swap">
<style>
  :root {
    --lime: #acd037;
    --lime-dark: #8fb424;
    --lime-light: #c4df5a;
    --coral: #f04a50;
    --ink: #0b0b0b;
    --paper: #f7f7f5;
    --white: #ffffff;
    --grey-line: #8a8a8a;
    --stamp-tone: #e4e4e4;
    --stage: #e9e7e2;
    --serif: "PT Serif", "Times New Roman", serif;
  }
  * { box-sizing: border-box; margin: 0; padding: 0; }
  html, body {
    width: 1200px; height: 780px; overflow: hidden;
    background: var(--stage);
    font-family: var(--serif);
  }
  .stage {
    width: 1200px; height: 780px;
    display: flex; align-items: center; justify-content: center; gap: 40px;
  }
  .card {
    position: relative;
    width: 540px; height: 310px;
    overflow: hidden;
    box-shadow: 0 6px 18px rgba(0,0,0,.18);
  }

  /* ---------- Brand block ---------- */
  .brand {
    position: absolute; left: 0; top: 0; width: 100%;
    display: flex; flex-direction: column; align-items: center; justify-content: center;
  }
  .brand__line { display: flex; align-items: center; gap: 14px; }
  .brand-dot { width: 32px; height: 32px; border-radius: 50%; background: var(--lime); }
  .brand-name {
    font-family: var(--serif); font-weight: 700;
    font-size: 34px; line-height: 1.1; color: var(--coral); letter-spacing: .5px;
  }
  .brand__tagline {
    margin-top: 6px; font-size: 15px; color: var(--ink); letter-spacing: 1.5px;
    text-transform: uppercase;
  }

  /* ---------- Front ---------- */
  .card--front { background: var(--paper); }
  .card--front .brand { height: 165px; }
  .front__band {
    position: absolute; left: 0; top: 165px; width: 100%; height: 145px;
    background: var(--ink);
    display: flex; align-items: center;
  }
  .person { width: 262px; padding-right: 16px; text-align: right; color: var(--white); }
  .person__name { color: var(--lime); font-size: 23px; line-height: 1.15; }
  .person__role { font-size: 16px; line-height: 1.25; }
  .person__addr { font-size: 15px; line-height: 1.3; }
  .divider { width: 1px; height: 96px; background: var(--grey-line); }
  .contact { padding-left: 16px; color: var(--white); font-size: 14px; line-height: 1.5; }
  .contact__row { display: flex; align-items: center; gap: 8px; }
  .contact__icon { width: 14px; height: 14px; flex: none; }
  .contact__abn { color: var(--lime); margin-top: 2px; }

  /* ---------- Back ---------- */
  .card--back {
    background: radial-gradient(ellipse at 55% 35%, var(--lime-light) 0%, var(--lime) 55%, var(--lime-dark) 100%);
  }
  .card--back .brand { height: 150px; }
  .card--back .brand-dot { background: var(--coral); }
  .stamp-band {
    position: absolute; left: 0; top: 158px; width: 100%; height: 72px;
    background: var(--ink);
    display: flex; align-items: center; justify-content: space-evenly;
    padding: 0 14px;
  }
  .stamp {
    width: 46px; height: 46px; border-radius: 50%;
    background: radial-gradient(circle at 40% 35%, var(--white) 0%, var(--stamp-tone) 100%);
  }
  .stamp--free {
    display: flex; align-items: center; justify-content: center;
    font-size: 15px; color: var(--ink);
  }
  .rounds {
    position: absolute; left: 0; top: 242px; width: 100%;
    display: flex; justify-content: center; gap: 12px;
  }
  .round {
    width: 14px; height: 14px; border-radius: 50%;
    border: 2px solid var(--ink); background: transparent;
  }
  .back__web {
    position: absolute; left: 0; top: 268px; width: 100%;
    text-align: center; font-size: 15px; color: var(--ink);
  }
</style>
</head>
<body>
<main class="stage">

  <section class="card card--front" aria-label="Business card front">
    <div class="brand">
      <div class="brand__line">
        <span class="brand-dot"></span>
        <span class="brand-name">Wrenfield Pantry</span>
      </div>
      <p class="brand__tagline">Products for Healthy Dogs</p>
    </div>
    <div class="front__band">
      <div class="person">
        <p class="person__name">Employee Name</p>
        <p class="person__role">Owner</p>
        <p class="person__addr">PO Box 4180</p>
        <p class="person__addr">GLENHAVEN VIC 3127</p>
      </div>
      <span class="divider"></span>
      <div class="contact">
        <p class="contact__row">
          <svg class="contact__icon" viewBox="0 0 14 14" aria-hidden="true">
            <rect width="14" height="14" fill="#acd037"/>
            <rect x="4.5" y="2.5" width="5" height="9" rx="1" fill="none" stroke="#0b0b0b" stroke-width="1.2"/>
          </svg>
          +0417 358 619
        </p>
        <p class="contact__row">
          <svg class="contact__icon" viewBox="0 0 14 14" aria-hidden="true">
            <rect width="14" height="14" fill="#acd037"/>
            <rect x="2.5" y="4" width="9" height="6.5" fill="none" stroke="#0b0b0b" stroke-width="1.1"/>
            <path d="M2.5 4 L7 8 L11.5 4" fill="none" stroke="#0b0b0b" stroke-width="1.1"/>
          </svg>
          info@wrenfieldpantry.com.au
        </p>
        <p class="contact__row">
          <svg class="contact__icon" viewBox="0 0 14 14" aria-hidden="true">
            <rect width="14" height="14" fill="#acd037"/>
            <circle cx="7" cy="7" r="4.3" fill="none" stroke="#0b0b0b" stroke-width="1.1"/>
            <path d="M2.7 7 H11.3 M7 2.7 C5 5 5 9 7 11.3 M7 2.7 C9 5 9 9 7 11.3" fill="none" stroke="#0b0b0b" stroke-width="0.9"/>
          </svg>
          www.wrenfieldpantry.com.au
        </p>
        <p class="contact__abn">ABN# 47 215 903 618</p>
      </div>
    </div>
  </section>

  <section class="card card--back" aria-label="Loyalty card back">
    <div class="brand">
      <div class="brand__line">
        <span class="brand-dot"></span>
        <span class="brand-name">Wrenfield Pantry</span>
      </div>
      <p class="brand__tagline">Products for Healthy Dogs</p>
    </div>
    <div class="stamp-band">
      <span class="stamp" role="img" aria-label="Dog head stamp area, purchase 1"></span>
      <span class="stamp" role="img" aria-label="Dog head stamp area, purchase 2"></span>
      <span class="stamp" role="img" aria-label="Dog head stamp area, purchase 3"></span>
      <span class="stamp" role="img" aria-label="Dog head stamp area, purchase 4"></span>
      <span class="stamp" role="img" aria-label="Dog head stamp area, purchase 5"></span>
      <span class="stamp" role="img" aria-label="Dog head stamp area, purchase 6"></span>
      <span class="stamp stamp--free">Free</span>
    </div>
    <div class="rounds" aria-label="Five reward rounds, one ring marked per completed round">
      <span class="round"></span>
      <span class="round"></span>
      <span class="round"></span>
      <span class="round"></span>
      <span class="round"></span>
    </div>
    <p class="back__web">www.wrenfieldpantry.com.au</p>
  </section>

</main>
</body>
</html>
```